Education related business need name card design

We need name card design for long term study agent.
Company name is Harbor Lantern.
We support clients to connect to the world.
Clients are Japanese family who has primary and secondary school students.

Company Logo is reflection of the globe and HL (Harbor Lantern).
Since business is related to education, we would like to show reliability and love to see the world map (atlas) in the name card.

Target Market(s)

late 30's to 50's parents of primary and secondary students who are enthusiastic for education. Secondary school management

Industry/Entity Type

Education

Contact Information for Business Card

Company name, Address, Official position, Name, Phone number, Mobile number, email address,

Font styles to use
Serif
Other font styles liked:
• Century Gothic(logo)

Requirements
Must have
• Since businee is related to education, we would like to show reliability and love to see the world map (atlas) in the name card.

```html
<!DOCTYPE html>
<html lang="en">
<head>
<meta charset="utf-8">
<title>Harbor Lantern Pte.Ltd. – Name Card</title>
<link rel="stylesheet" href="https://fonts.googleapis.com/css2?family=Questrial&display=swap">
<style>
  :root {
    --stage: #e9e7e4;
    --card: #f7f7f6;
    --navy: #0b3a8c;
    --brand: #1a4ea3;
    --sky: #1f7fd3;
    --ink: #1d3f86;
    --white: #ffffff;
  }
  * { box-sizing: border-box; margin: 0; padding: 0; }
  html, body {
    width: 1200px; height: 768px; overflow: hidden;
    background: var(--stage);
    font-family: "Questrial", "Century Gothic", sans-serif;
  }
  .stage { position: relative; width: 1200px; height: 768px; }
  .card {
    position: absolute; top: 234px;
    width: 520px; height: 300px;
    background: var(--card);
    box-shadow: 0 6px 18px rgba(0,0,0,.18);
    overflow: hidden;
  }
  .card--front { left: 50px; }
  .card--back { left: 630px; }

  /* front */
  .front-brand {
    position: absolute; inset: 0;
    display: flex; flex-direction: column; align-items: center; justify-content: center;
    gap: 18px;
  }
  .brand-dot { width: 74px; height: 74px; border-radius: 50%; background: var(--sky); }
  .front-brand .brand-name { font-size: 30px; color: var(--brand); letter-spacing: .2px; }

  /* back */
  .back-brand {
    position: absolute; left: 34px; top: 26px;
    display: flex; align-items: center; gap: 12px;
  }
  .back-brand .brand-dot { width: 40px; height: 40px; }
  .back-brand .brand-name { font-size: 20px; line-height: 1.05; color: var(--brand); }

  .contacts {
    position: absolute; left: 34px; top: 92px;
    list-style: none; font-size: 13.5px; color: var(--ink); line-height: 1.3;
  }
  .contacts li { display: flex; align-items: center; gap: 10px; }
  .contacts svg { width: 11px; height: 11px; fill: var(--ink); flex: none; }
  .contacts .address { display: block; width: 190px; }

  .wave { position: absolute; inset: 0; width: 520px; height: 300px; }
  .person {
    position: absolute; right: 30px; bottom: 16px; text-align: right; color: var(--white);
  }
  .person .name { font-size: 22px; letter-spacing: .3px; line-height: 1.2; }
  .person .title { font-size: 13px; margin-top: 4px; }
</style>
</head>
<body>
<main class="stage">

  <section class="card card--front" aria-label="Card front">
    <div class="front-brand">
      <span class="brand-dot" aria-hidden="true"></span>
      <span class="brand-name">Harbor Lantern Pte.Ltd.</span>
    </div>
  </section>

  <section class="card card--back" aria-label="Card back">
    <svg class="wave" viewBox="0 0 520 300" aria-hidden="true">
      <path fill="none" stroke="var(--sky)" stroke-width="7" d="M0,188 C90,238 200,250 290,232 C380,214 450,180 520,158"/>
      <path fill="none" stroke="var(--sky)" stroke-width="3" opacity=".8" d="M0,196 C80,240 170,252 260,246"/>
      <path fill="var(--navy)" d="M0,204 C90,254 200,266 290,248 C380,230 450,196 520,174 L520,300 L0,300Z"/>
    </svg>

    <div class="back-brand">
      <span class="brand-dot" aria-hidden="true"></span>
      <span class="brand-name">Harbor Lantern<br>Pte.Ltd.</span>
    </div>

    <ul class="contacts">
      <li><svg viewBox="0 0 12 12" aria-hidden="true"><path d="M1 3 Q1 1 3 1 L9 1 Q11 1 11 3 L11 4 L8 4 L8 3 L4 3 L4 4 L1 4Z M2 5 L10 5 L11 11 L1 11Z"/></svg>+00 111 222 3333</li>
      <li><svg viewBox="0 0 12 12" aria-hidden="true"><path d="M0 2 L12 2 L12 10 L0 10Z M1 3 L6 7 L11 3" stroke="#f7f7f6" stroke-width="1"/></svg>yourname@yourwebsite.com</li>
      <li><svg viewBox="0 0 12 12" aria-hidden="true"><circle cx="6" cy="6" r="5.5"/><path d="M0.5 6 H11.5 M6 0.5 V11.5" stroke="#f7f7f6" stroke-width="1"/></svg>www.yourwebsite.com</li>
      <li class="address">Your Long Commercial or business address in 2 line</li>
    </ul>

    <div class="person">
      <p class="name">Your Long name</p>
      <p class="title">Your Title</p>
    </div>
  </section>

</main>
</body>
</html>
```